"Harrow Crest Builders" is a residential building company and needs a new business card design and may re

We would like a redesign based on the existing logo, and would like to see a new font as well. We are bespoke home builders who build sustainable energy efficient homes.

Industry/Entity Type

Construction

Contact Information for Business Card

Business card size 40mm x 90mm

Colors

Designer to choose colors to be used in the design.

```html
<!DOCTYPE html>
<html lang="en">
<head>
<meta charset="utf-8">
<title>Harrow Crest Builders – Business Card</title>
<link rel="stylesheet" href="https://fonts.googleapis.com/css2?family=Figtree:wght@400;500;700&display=swap">
<style>
  :root {
    --ink: #111111;
    --paper: #ffffff;
    --brand-yellow: #fdd64b;
    --pattern-dark: #1c1c1c;
    --pattern-mid: #4a4a4a;
  }
  * { margin: 0; padding: 0; box-sizing: border-box; }
  html, body { width: 1200px; height: 1200px; overflow: hidden; background: var(--paper); }
  body { position: relative; font-family: "Figtree", Arial, sans-serif; color: var(--ink); }

  .card {
    position: absolute;
    left: 146px;
    width: 909px;
    border: 1.5px solid var(--ink);
    background: var(--paper);
    overflow: hidden;
  }
  .card--front { top: 162px; height: 413px; }
  .card--back  { top: 640px; height: 405px; }

  .pattern-field {
    position: absolute; inset: 0;
    background: linear-gradient(135deg, var(--pattern-dark), var(--pattern-mid));
  }

  .brand-panel {
    position: absolute;
    left: 299px; top: 50px;
    width: 311px; height: 311px;
    background: var(--paper);
    border: 1.5px solid var(--ink);
    display: flex; flex-direction: column; align-items: center; justify-content: center;
    color: var(--brand-yellow);
    font-weight: 700;
    text-align: center;
  }
  .brand-panel__mark {
    width: 110px; height: 110px;
    background: var(--brand-yellow);
    margin-bottom: 26px;
  }
  .brand-panel__name { font-size: 41px; line-height: 1; letter-spacing: -1px; }
  .brand-panel__sub  { font-size: 32px; line-height: 1.15; letter-spacing: -0.8px; }

  .back__disc {
    position: absolute;
    left: 322px; top: 56px;
    width: 264px; height: 264px;
    border-radius: 50%;
    background: var(--brand-yellow);
  }
  .contact__name,
  .contact__phone,
  .legal {
    position: absolute;
    left: 0; right: 0;
    text-align: center;
    white-space: nowrap;
  }
  .contact__name  { top: 154px; font-size: 36px; font-weight: 700; line-height: 44px; letter-spacing: -0.4px; }
  .contact__phone { top: 205px; font-size: 37px; font-weight: 400; line-height: 48px; letter-spacing: -0.4px; }
  .legal          { top: 352px; font-size: 22px; line-height: 26px; letter-spacing: -0.2px; }

  .vertical {
    position: absolute;
    font-size: 22px;
    line-height: 26px;
    white-space: nowrap;
    top: 50%;
  }
  .vertical--company {
    left: 88px;
    transform: translate(-50%, -50%) rotate(-90deg);
    margin-top: 18px;
  }
  .vertical--email {
    left: 832px;
    transform: translate(-50%, -50%) rotate(90deg);
    margin-top: -2px;
  }
</style>
</head>
<body>

<section class="card card--front">
  <div class="pattern-field" role="img" aria-label="Repeating brand pattern in black on white"></div>
  <div class="brand-panel">
    <div class="brand-panel__mark"></div>
    <div class="brand-panel__name">Harrow Crest</div>
    <div class="brand-panel__sub">builders</div>
  </div>
</section>

<section class="card card--back">
  <div class="back__disc"></div>
  <div class="vertical vertical--company">Harrow Crest Builders Pty Ltd</div>
  <p class="contact__name">Daniel Voss</p>
  <p class="contact__phone">0412 555 019</p>
  <p class="legal">Registration 40718 ABN: 52 904 318 667</p>
  <div class="vertical vertical--email">daniel@harrowcrestbuilders.com.au</div>
</section>

</body>
</html>
```